Web Design Project (Mente Lumo)

We are going to do a therapy template to a psychologist. The site already exists, adress: www.mentelumo.net. So, its a total redesign job. I'm from Brazil, the language is PT-BR, so I'm gonna translate what you think be necessary. You can use the current structure from the website as a base to the new design. Check this template to see what I usually like: http://www.layoutkiosk.example/demo/51937.html
Updates

I'm waiting for new creative designs. The 'structure' image is just for 'pb'.

Requirements
Must have
• We need a modern menu, it should use a cool font style and make some kind of effect and little noise when the user pass over with the mouse (FLASH/HTML 5). The main page must emphasize the fact that we offer online treatment, like a picture or frame saying "Online Treatment, click here". It must also show the therapist picture and her name. The colors need to pass a tranquility feeling. The clinic telephone must always be present, doesn't matter which page the user is. The website must adapt to any resolution above 1024x768, crossbrowsing and accept javascript (I'll use www.agendrix.example, so its necessary embed code)
Nice to have
• I would appreciate if there was some kind of slow background animation, passing behind the text using the transparency.
Should not have
• Can't take too long to load, and won't have news or blog

```html
<!DOCTYPE html>
<html lang="pt-BR">
<head>
<meta charset="utf-8">
<title>Mente Lumo</title>
<link rel="stylesheet" href="https://fonts.googleapis.com/css2?family=PT+Sans:wght@400;700&family=Pinyon+Script&display=swap">
<style>
:root{
  --teal-dark:#2f7f96;
  --teal:#4a9bb1;
  --teal-light:#6fb3c6;
  --hero-top:#bcd5dd;
  --hero-bottom:#e6eef1;
  --ink:#1f2b30;
  --quote:#1d4756;
  --heading:#1b7b8c;
  --link:#1b6e86;
  --white:#ffffff;
  --red-top:#f0283c;
  --red-bottom:#fa5868;
  --cyan-top:#00c6dd;
  --cyan-bottom:#0aaec6;
  --head-blue:#2f8fe0;
  --map-tone:#e8e2d4;
  --dot-dark:#0c0c0c;
  --dot-active:#6fd43a;
}
*{margin:0;padding:0;box-sizing:border-box}
html,body{width:1200px;height:1160px;overflow:hidden}
body{font-family:"PT Sans",sans-serif;color:var(--ink);background:#e9f0f2;position:relative}
.abs{position:absolute}
a{text-decoration:none}

/* header */
.site-header{left:0;top:0;width:1200px;height:155px;
  background:linear-gradient(180deg,var(--teal-light) 0%,var(--teal) 45%,var(--teal-dark) 100%);
  border-bottom:2px solid #d9ebf0}
.brand{left:48px;top:44px;display:flex;align-items:center;gap:14px}
.brand-mark{width:58px;height:58px;border-radius:50%;background:#cfe3c8}
.brand-name{font-size:38px;font-weight:700;color:#e6f0e2;line-height:1}
.main-nav{left:0;top:0;width:1200px;height:100px}
.main-nav a{position:absolute;top:68px;font-size:15px;color:var(--white);letter-spacing:.2px}
.main-nav a.active{top:0;left:394px;width:88px;height:100px;padding-top:68px;text-align:center;
  color:#1e3a44;background:linear-gradient(180deg,#fff 0%,#f2f6f7 60%,#d9e2e5 100%);border-radius:0 0 4px 4px}

/* hero */
.hero{left:0;top:157px;width:1200px;height:391px;background:linear-gradient(180deg,var(--hero-top),var(--hero-bottom))}
.hero-quote{left:123px;top:82px;width:562px;font-family:"Pinyon Script",cursive;font-size:33px;line-height:43px;color:var(--quote)}
.hero-quote span{display:block;text-align:justify;text-align-last:justify;white-space:nowrap}
.hero-quote span.short{text-align-last:left}
.hero-art{left:752px;top:20px;width:310px;height:348px;background:radial-gradient(ellipse at 50% 40%,#4aa3ec,var(--head-blue));border-radius:48% 52% 30% 40%/45% 50% 30% 30%}
.slider-dots{left:383px;top:349px;display:flex;gap:12px}
.slider-dots span{width:13px;height:13px;border-radius:50%;background:var(--dot-dark)}
.slider-dots span.on{background:var(--dot-active)}

/* content */
.content{left:16px;top:548px;width:1162px;height:507px;background:var(--white)}
.about{left:25px;top:36px;width:370px}
.about h2{font-size:28px;font-weight:400;color:var(--heading);margin-bottom:8px}
.about-media{display:flex;align-items:flex-end;gap:16px;margin-bottom:10px}
.about-photo{width:190px;height:195px;background:linear-gradient(180deg,#9b9b9b,#d8d8d8);border-radius:40% 40% 10% 10%}
.about-name{font-size:16px;color:var(--heading);padding-bottom:4px}
.about p{font-size:13px;line-height:20px;text-align:justify}
.about p + p{margin-top:4px}
.about .more{display:block;margin-top:6px;margin-left:4px;font-size:13px;color:var(--link)}

.feature{left:421px;top:44px;width:399px;height:378px;border-radius:6px;
  background:linear-gradient(180deg,#f3f5f6,#fff 30%,#fff 80%,#eef1f2);box-shadow:0 10px 10px -8px rgba(0,0,0,.25);border:1px solid #eef2f3}
.feature-head{position:absolute;left:36px;top:24px;display:flex;align-items:center;gap:12px;font-size:21px;color:#233a48;letter-spacing:.3px}
.feature-rule{position:absolute;left:32px;top:66px;width:342px;height:1px;background:#c9d2d6}
.feature-text{position:absolute;left:37px;top:90px;width:318px;font-size:13px;line-height:17.6px;color:#2a2f33}
.feature-text p{margin-bottom:17px}
.feature .more{position:absolute;left:301px;top:320px;font-size:16px;color:var(--link)}

.cta{left:855px;width:293px;border-radius:5px;color:var(--white);display:flex;align-items:center}
.cta-online{top:45px;height:91px;background:linear-gradient(180deg,var(--red-top),var(--red-bottom))}
.cta-online .label{margin-left:14px;font-size:18px;line-height:22px}
.cta-online .label small{font-size:16px}
.cta-phone{top:152px;height:92px;background:linear-gradient(180deg,var(--cyan-top),var(--cyan-bottom))}
.cta-phone .number{margin-left:18px;font-size:29px;letter-spacing:.5px}
.map{left:855px;top:258px;width:293px;height:163px;border:2px solid #1b6e86;border-radius:5px;background:linear-gradient(135deg,#e7e4db,var(--map-tone))}

/* footer */
.site-footer{left:0;top:1055px;width:1200px;height:105px;background:linear-gradient(180deg,#2c7088 0,#2c7088 4px,#3f8aa2 5px,#4a97ae 100%)}
.footer-address{left:63px;top:36px;font-size:13px;line-height:21px;color:#0f1e24}
.footer-nav{right:33px;top:32px;font-size:13px;color:#0f1e24}
.footer-nav a{color:#0f1e24}
.footer-nav .sep{margin:0 7px}
.footer-copy{right:33px;top:67px;font-size:13px;color:#0f1e24}
</style>
</head>
<body>

<header class="site-header abs">
  <div class="brand abs">
    <span class="brand-mark"></span>
    <span class="brand-name">Mente Lumo</span>
  </div>
  <nav class="main-nav abs">
    <a class="active" href="#">HOME</a>
    <a style="left:492px" href="#">ONLINE SERVICE</a>
    <a style="left:634px" href="#">TREATMENTS</a>
    <a style="left:755px" href="#">QUESTIONS</a>
    <a style="left:865px" href="#">ASK THE EXPERT</a>
    <a style="left:1004px" href="#">LOCATION</a>
    <a style="left:1110px" href="#">CONTACT</a>
  </nav>
</header>

<section class="hero abs">
  <p class="hero-quote abs">
    <span>"É vital conhecermos nossos pensamentos</span>
    <span>para termos controle sobre eles e assim</span>
    <span class="short">nutri-los, dirigi-los, expandi-los,</span>
    <span class="short">reduzi-los ou rejeitá-los."</span>
  </p>
  <div class="hero-art abs" role="img" aria-label="Illustration of a blue head in profile filled with gears"></div>
  <div class="slider-dots abs"><span></span><span></span><span class="on"></span></div>
</section>

<main class="content abs">
  <section class="about abs">
    <h2>About Me</h2>
    <div class="about-media">
      <div class="about-photo" role="img" aria-label="Black and white portrait of the therapist"></div>
      <span class="about-name">Dra. Lara Quintel</span>
    </div>
    <p>A Terapia Cognitiva tem como método a interpretação de processos e conteúdos mentais (as cognições),</p>
    <p>e sua influência na vida cotidiana. O comportamento e a emoção vêm depois do processamento cognitivo. É vital conhecermos nossos pensamentos para termos controle sobre eles, e assim podemos: nutri-los, expandi-los, reduzi-los ou rejeitá-los.</p>
    <a class="more" href="#">More &gt;&gt;</a>
  </section>

  <section class="feature abs">
    <div class="feature-head">
      <svg width="26" height="20" viewBox="0 0 26 20" aria-hidden="true">
        <rect x="1" y="3" width="20" height="15" fill="#e9eef1" stroke="#7d93a0"/>
        <line x1="4" y1="8" x2="16" y2="8" stroke="#3a7fc0" stroke-width="2"/>
        <line x1="4" y1="12" x2="14" y2="12" stroke="#7d93a0"/>
        <line x1="4" y1="15" x2="12" y2="15" stroke="#7d93a0"/>
        <path d="M15 14 L24 3 L26 5 L17 16 Z" fill="#e8a23a"/>
      </svg>
      <span>COGNITIVE THERAPY</span>
    </div>
    <div class="feature-rule"></div>
    <div class="feature-text">
      <p>Lorem Ipsum is simply dummy text of the printing and typesetting industry.Lorem Ipsum is simply dummy text of the printing and typesetting industry.</p>
      <p>Lorem Ipsum is simply dummy text of the printing and typesetting industry.Lorem Ipsum is simply dummy text of the printing and typesetting industry.</p>
      <p>Lorem Ipsum is simply dummy text of the printing and typesetting industry.Lorem Ipsum is simply dummy text of the printing and typesetting industry.</p>
    </div>
    <a class="more" href="#">MORE &nbsp;&gt;&gt;</a>
  </section>

  <a class="cta cta-online abs" href="#">
    <svg width="62" height="64" viewBox="0 0 62 64" style="margin-left:12px" aria-hidden="true">
      <path d="M8 38 V30 A23 23 0 0 1 54 30 V38" fill="none" stroke="#333" stroke-width="5"/>
      <rect x="4" y="34" width="14" height="24" rx="6" fill="#2a2a2a"/>
      <rect x="44" y="34" width="14" height="24" rx="6" fill="#2a2a2a"/>
      <circle cx="11" cy="46" r="5" fill="#3d9be0"/>
      <circle cx="51" cy="46" r="5" fill="#3d9be0"/>
    </svg>
    <span class="label">ATENDIMENTO ONLINE<br><small>- CLIQUE AQUI</small></span>
  </a>

  <div class="cta cta-phone abs">
    <svg width="44" height="50" viewBox="0 0 44 50" style="margin-left:22px" aria-hidden="true">
      <path d="M10 2 L17 2 L20 14 L14 18 C16 27 21 33 28 37 L33 31 L43 36 L42 45 C38 49 32 49 26 46 C14 39 6 28 3 15 C2 8 5 4 10 2 Z" fill="#1a1a1a"/>
    </svg>
    <span class="number">(11)3555-0192</span>
  </div>

  <div class="map abs" role="img" aria-label="Street map showing the clinic location"></div>
</main>

<footer class="site-footer abs">
  <div class="footer-address abs">
    Rua Vale Sereno, 140, 7º andar, Sala 73 - Centro - São Lumo, SP<br>
    Clique aqui para ver o mapa<br>
    Email : contato@mentelumo.net
  </div>
  <nav class="footer-nav abs">
    <a href="#">Home</a><span class="sep">|</span><a href="#">Online Service</a><span class="sep">|</span><a href="#">Treatments</a><span class="sep">|</span><a href="#">Questions</a><span class="sep">|</span><a href="#">Ask the expert</a><span class="sep">|</span><a href="#">Location</a>
  </nav>
  <div class="footer-copy abs">© 2012 &nbsp;mentelumo &nbsp;| &nbsp;All right reserved</div>
</footer>

</body>
</html>
```